Elder abuse Infographic Poster for doctor surgeries

I am looking for someone to redesign, or clean up an infographic poster that we have drafted to raise awareness for Elder abuse. The colour for elder abuse is deep dark purple, and we would like it to be high resolution so it can be printed A3 size and placed in Doctor surgeries. The poster will be used by a not-for-profit in Australia. We are looking to use pictures, rather than heavy text blocks, following the Infographic poster style (I have included a couple of infographic posters for inspiration).
Reason: Providing extra time for more designs :)
Target Market(s)
Older people, 60+
Industry/Entity Type
Doctor
Requirements
Nice to have
- NOTE: You do not need to use the banner etc I have attached, its just an idea for the colours we use etc.
Should not have
- Images of frail older people, pastel colourings, or anything typically associated with frail aged.

```html
<!DOCTYPE html>
<html lang="en">
<head>
<meta charset="utf-8">
<title>There Is No Excuse For Elder Abuse – Poster</title>
<link rel="stylesheet" href="https://fonts.googleapis.com/css2?family=Roboto+Condensed:wght@400;700&family=Ubuntu:wght@300;400&display=swap">
<style>
:root{
  --purple:#46368a;
  --sky:#c5e5f7;
  --pink:#d6569e;
  --ink:#1d4a9c;
  --white:#ffffff;
  --frame:#3a5ba8;
}
*{box-sizing:border-box;margin:0;padding:0}
html,body{width:1200px;height:1000px;overflow:hidden;background:var(--white)}
body{position:relative;font-family:"Roboto Condensed",Arial,sans-serif;border:1px solid #9db3de}
.poster{position:absolute;left:284px;top:68px;width:612px;height:864px;border:1px solid var(--frame);background:var(--white);overflow:hidden}
.block{position:absolute}

/* headline */
.headline{left:26px;top:52px;width:300px;font-weight:300}
.headline .line{position:absolute;left:0;display:flex;column-gap:10px}
.word{display:flex}
.word span{display:inline-block;background:var(--purple);color:var(--white);font-family:"Ubuntu",Arial,sans-serif;font-weight:300;font-size:54px;line-height:58px;padding:0 2px}
.word span:nth-child(3n+1){transform:translateY(-4px);padding-bottom:3px}
.word span:nth-child(3n+2){transform:translateY(3px)}
.word span:nth-child(4n){padding-top:5px}

/* risk factors */
.risk{left:334px;top:0;width:278px;height:178px;background:var(--purple);color:var(--white);padding:18px 0 0 8px}
.risk h2{font-size:23px;font-weight:700;letter-spacing:-.5px;margin-bottom:8px}
.risk ul{list-style:none;padding-left:38px}
.risk li{display:flex;align-items:center;height:30px;font-size:16px}
.risk svg{width:22px;height:22px;margin-right:15px;margin-left:-2px}

/* types of abuse */
.types{left:334px;top:178px;width:278px;height:312px;background:var(--sky);color:var(--ink);padding:30px 0 0 18px}
.types h2{font-size:29px;font-weight:400;margin-bottom:14px;letter-spacing:-.3px}
.types ul{list-style:none}
.types li{display:grid;grid-template-columns:12px auto 1fr;column-gap:10px;align-items:start;min-height:40px;font-size:11.5px;line-height:13px}
.types li::before{content:"";width:8px;height:8px;border-radius:50%;background:var(--ink);margin-top:3px}
.types b{font-size:13.5px;font-weight:700;line-height:15px}
.types span{padding-top:2px}

/* statistic banner */
.stat{left:0;top:490px;width:612px;height:112px;background:var(--purple);color:var(--white);text-align:center;padding-top:14px}
.stat h2{font-size:23px;font-weight:700;letter-spacing:-.5px}
.people{display:flex;justify-content:center;gap:1px;margin-top:6px;margin-left:-2px}
.people svg{width:42px;height:44px}

/* prevention / stopping */
.actions{left:0;top:602px;width:612px;height:152px;background:var(--sky);color:var(--ink)}
.col{position:absolute;top:16px}
.col h2{font-size:26px;font-weight:400;letter-spacing:-.3px;margin-bottom:4px}
.col ul{list-style:none}
.col li{font-size:11px;line-height:14px;padding-left:18px;position:relative;margin-bottom:4px}
.col li::before{content:"";position:absolute;left:2px;top:4px;width:7px;height:7px;border-radius:50%;background:var(--ink)}
.prevention{left:31px;width:300px}
.stopping{left:344px;width:260px;top:14px}

/* footer */
.helpline{left:0;top:754px;width:306px;height:110px;background:var(--purple);color:var(--white)}
.helpline .phone{position:absolute;left:42px;top:14px;width:34px;height:46px}
.helpline h3{position:absolute;left:82px;top:12px;font-size:16px;font-weight:700;letter-spacing:.3px}
.helpline .number{position:absolute;left:109px;top:32px;font-size:21px;font-weight:400}
.helpline .lead{position:absolute;left:60px;top:70px;font-size:9.5px;font-weight:700;letter-spacing:.4px}
.helpline .traits{position:absolute;left:180px;top:70px;font-size:9.5px;font-weight:700;line-height:11px;letter-spacing:.4px;list-style:none}
.org{left:306px;top:754px;width:306px;height:110px;display:flex;align-items:center;justify-content:center;gap:10px}
.org .mark{width:18px;height:18px;border-radius:50%;background:var(--pink)}
.org .name{font-size:30px;font-weight:700;color:var(--pink);letter-spacing:-.5px}
</style>
</head>
<body>
<main class="poster">

  <h1 class="block headline" aria-label="There is no excuse for elder abuse">
    <div class="line" style="top:0"><span class="word"><span>t</span><span>h</span><span>e</span><span>r</span><span>e</span></span></div>
    <div class="line" style="top:82px"><span class="word"><span>i</span><span>s</span></span><span class="word"><span>n</span><span>o</span></span></div>
    <div class="line" style="top:164px"><span class="word"><span>e</span><span>x</span><span>c</span><span>u</span><span>s</span><span>e</span></span></div>
    <div class="line" style="top:248px;left:4px"><span class="word"><span>f</span><span>o</span><span>r</span></span><span class="word"><span>e</span><span>l</span><span>d</span><span>e</span><span>r</span></span></div>
    <div class="line" style="top:332px;left:4px"><span class="word"><span>a</span><span>b</span><span>u</span><span>s</span><span>e</span></span></div>
  </h1>

  <section class="block risk">
    <h2>RISK FACTORS</h2>
    <ul>
      <li><svg viewBox="0 0 22 22"><path d="M9 2h4v7h7v4h-7v7H9v-7H2V9h7z" fill="var(--pink)"/></svg>Illness</li>
      <li><svg viewBox="0 0 22 22"><circle cx="11" cy="11" r="9" fill="none" stroke="var(--pink)" stroke-width="2"/><circle cx="11" cy="11" r="5" fill="none" stroke="var(--pink)" stroke-width="1.5"/><path d="M11 8v6" stroke="var(--pink)" stroke-width="1.5"/></svg>Difficulty managing money</li>
      <li><svg viewBox="0 0 22 22"><path d="M10 1h2v7c3 1 4 5 5 11H5c1-6 2-10 5-11z" fill="var(--pink)"/><circle cx="11" cy="20.5" r="1.5" fill="var(--pink)"/></svg>Dependence</li>
      <li><svg viewBox="0 0 22 22"><path d="M3 10L11 3l8 7v9H3z" fill="none" stroke="var(--pink)" stroke-width="2"/><path d="M9 19v-5h4v5" fill="none" stroke="var(--pink)" stroke-width="2"/></svg>Isolation</li>
    </ul>
  </section>

  <section class="block types">
    <h2>TYPES OF ABUSE</h2>
    <ul>
      <li><b>Psychological</b><span>bullying, shouting,<br>swearing</span></li>
      <li><b>Social</b><span>Stopping access to family/friends</span></li>
      <li><b>Financial</b><span>Taking money, not allowing<br>access to accounts</span></li>
      <li><b>Neglect</b><span>Withholding essential care</span></li>
      <li><b>Sexual</b><span>Inappropriate touching,<br>comments</span></li>
      <li><b>Hitting</b><span>slapping, physical harm</span></li>
    </ul>
  </section>

  <section class="block stat">
    <h2>1 In 20 OLDER PEOPLE WILL EXPERIENCE ELDER ABUSE</h2>
    <div class="people" role="img" aria-label="Ten person icons, one highlighted">
      <svg viewBox="0 0 42 44"><circle cx="25" cy="13" r="9" fill="var(--white)"/><path d="M9 44c0-13 7-20 16-20s16 7 16 20z" fill="var(--white)"/><circle cx="13" cy="16" r="8" fill="var(--white)" stroke="var(--purple)" stroke-width="2"/><path d="M1 44c0-11 5-17 12-17s12 6 12 17z" fill="var(--white)" stroke="var(--purple)" stroke-width="2"/></svg>
      <svg viewBox="0 0 42 44"><circle cx="25" cy="13" r="9" fill="var(--pink)"/><path d="M9 44c0-13 7-20 16-20s16 7 16 20z" fill="var(--pink)"/><circle cx="13" cy="16" r="8" fill="var(--white)" stroke="var(--purple)" stroke-width="2"/><path d="M1 44c0-11 5-17 12-17s12 6 12 17z" fill="var(--white)" stroke="var(--purple)" stroke-width="2"/></svg>
      <svg viewBox="0 0 42 44"><circle cx="25" cy="13" r="9" fill="var(--white)"/><path d="M9 44c0-13 7-20 16-20s16 7 16 20z" fill="var(--white)"/><circle cx="13" cy="16" r="8" fill="var(--white)" stroke="var(--purple)" stroke-width="2"/><path d="M1 44c0-11 5-17 12-17s12 6 12 17z" fill="var(--white)" stroke="var(--purple)" stroke-width="2"/></svg>
      <svg viewBox="0 0 42 44"><circle cx="25" cy="13" r="9" fill="var(--white)"/><path d="M9 44c0-13 7-20 16-20s16 7 16 20z" fill="var(--white)"/><circle cx="13" cy="16" r="8" fill="var(--white)" stroke="var(--purple)" stroke-width="2"/><path d="M1 44c0-11 5-17 12-17s12 6 12 17z" fill="var(--white)" stroke="var(--purple)" stroke-width="2"/></svg>
      <svg viewBox="0 0 42 44"><circle cx="25" cy="13" r="9" fill="var(--white)"/><path d="M9 44c0-13 7-20 16-20s16 7 16 20z" fill="var(--white)"/><circle cx="13" cy="16" r="8" fill="var(--white)" stroke="var(--purple)" stroke-width="2"/><path d="M1 44c0-11 5-17 12-17s12 6 12 17z" fill="var(--white)" stroke="var(--purple)" stroke-width="2"/></svg>
      <svg viewBox="0 0 42 44"><circle cx="25" cy="13" r="9" fill="var(--white)"/><path d="M9 44c0-13 7-20 16-20s16 7 16 20z" fill="var(--white)"/><circle cx="13" cy="16" r="8" fill="var(--white)" stroke="var(--purple)" stroke-width="2"/><path d="M1 44c0-11 5-17 12-17s12 6 12 17z" fill="var(--white)" stroke="var(--purple)" stroke-width="2"/></svg>
      <svg viewBox="0 0 42 44"><circle cx="25" cy="13" r="9" fill="var(--white)"/><path d="M9 44c0-13 7-20 16-20s16 7 16 20z" fill="var(--white)"/><circle cx="13" cy="16" r="8" fill="var(--white)" stroke="var(--purple)" stroke-width="2"/><path d="M1 44c0-11 5-17 12-17s12 6 12 17z" fill="var(--white)" stroke="var(--purple)" stroke-width="2"/></svg>
      <svg viewBox="0 0 42 44"><circle cx="25" cy="13" r="9" fill="var(--white)"/><path d="M9 44c0-13 7-20 16-20s16 7 16 20z" fill="var(--white)"/><circle cx="13" cy="16" r="8" fill="var(--white)" stroke="var(--purple)" stroke-width="2"/><path d="M1 44c0-11 5-17 12-17s12 6 12 17z" fill="var(--white)" stroke="var(--purple)" stroke-width="2"/></svg>
      <svg viewBox="0 0 42 44"><circle cx="25" cy="13" r="9" fill="var(--white)"/><path d="M9 44c0-13 7-20 16-20s16 7 16 20z" fill="var(--white)"/><circle cx="13" cy="16" r="8" fill="var(--white)" stroke="var(--purple)" stroke-width="2"/><path d="M1 44c0-11 5-17 12-17s12 6 12 17z" fill="var(--white)" stroke="var(--purple)" stroke-width="2"/></svg>
      <svg viewBox="0 0 42 44"><circle cx="25" cy="13" r="9" fill="var(--white)"/><path d="M9 44c0-13 7-20 16-20s16 7 16 20z" fill="var(--white)"/><circle cx="13" cy="16" r="8" fill="var(--white)" stroke="var(--purple)" stroke-width="2"/><path d="M1 44c0-11 5-17 12-17s12 6 12 17z" fill="var(--white)" stroke="var(--purple)" stroke-width="2"/></svg>
    </div>
  </section>

  <section class="block actions">
    <div class="col prevention">
      <h2>PREVENTION</h2>
      <ul>
        <li>Stay connected to friends, family and community</li>
        <li>Know your rights!</li>
        <li>Access professional services to prevent dependence on family</li>
        <li>Consult a lawyer before signing any agreements</li>
      </ul>
    </div>
    <div class="col stopping">
      <h2>STOPPING ABUSE</h2>
      <ul>
        <li>Speak to your health professional</li>
        <li>Contact an advocate</li>
        <li>Consult a lawyer</li>
        <li>Elder abuse is often a crime!<br>If you are in danger, contact the Police 000</li>
      </ul>
    </div>
  </section>

  <section class="block helpline">
    <svg class="phone" viewBox="0 0 34 46" aria-hidden="true"><path d="M6 3l7-2 4 11-5 3c1 7 5 13 10 17l5-3 7 9-5 5C17 43 4 27 3 9z" fill="var(--pink)"/></svg>
    <h3>ELDER ABUSE HELPLINE</h3>
    <p class="number">1300 555 018</p>
    <p class="lead">Elder Abuse Helpline is</p>
    <ul class="traits"><li>Confidential</li><li>Client focused</li><li>Independent</li></ul>
  </section>

  <section class="block org">
    <span class="mark" aria-hidden="true"></span>
    <span class="name">Kinsafe Incorporated</span>
  </section>

</main>
</body>
</html>
```